Using attached logo that has been created

Business card with logo that's attached. Maybe with water or the cartoon van in background. Looking for it to not be so plain and not too white.
Information to include;
Dario Whitlock
(555) 208-7713
Info@mossbrookpipeworks.example
www.mossbrookpipeworks.example
License # 5320417
Looking forward to the designs u come up with.
Thank you!
-Teresa
The designer (Brynn), that I would like to work with requested an extension to allow time to create a couple designs for this project.
Target Market(s)
Plumbing
Industry/Entity Type
Plumbing
Contact Information for Business Card
Listed above
Font styles to use
Look and feel

```html
<!DOCTYPE html>
<html lang="en">
<head>
<meta charset="utf-8">
<title>Mossbrook Pipeworks – Business Card</title>
<link rel="stylesheet" href="https://fonts.googleapis.com/css2?family=Poppins:wght@400;500;700&display=swap">
<style>
  :root {
    --page-bg: #d6d8da;
    --brand-blue: #1a5cb0;
    --band-blue: #1767c2;
    --band-blue-dark: #1452a8;
    --accent-yellow: #f5b915;
    --water-light: #2e8fdc;
    --water-deep: #176fc4;
    --frost-light: #f7f7f8;
    --frost-mid: #e4e6e8;
    --ink: #222a33;
    --white: #ffffff;
    --mascot-front-a: #3f7fd0;
    --mascot-front-b: #2a68bd;
    --mascot-back-a: #c9d6e8;
    --mascot-back-b: #b3c4dc;
  }
  * { box-sizing: border-box; margin: 0; padding: 0; }
  html, body {
    width: 1187px;
    height: 1200px;
    overflow: hidden;
    background: var(--page-bg);
    font-family: "Poppins", sans-serif;
  }
  .card {
    position: absolute;
    left: 215px;
    width: 756px;
    height: 432px;
    border-radius: 18px;
    overflow: hidden;
  }
  .card--front { top: 122px; }
  .card--back { top: 644px; }

  .water-bg { position: absolute; inset: 0; }
  .card--front .water-bg {
    background: radial-gradient(ellipse at 50% 40%, var(--water-light), var(--water-deep) 80%);
  }
  .card--back .water-bg {
    background: radial-gradient(ellipse at 45% 45%, var(--frost-light), var(--frost-mid) 85%);
  }

  .mascot {
    position: absolute;
    border-radius: 28px;
  }
  .card--front .mascot {
    left: 313px; top: 28px; width: 190px; height: 246px;
    background: linear-gradient(180deg, var(--mascot-front-a), var(--mascot-front-b));
  }
  .card--back .mascot {
    left: 471px; top: 26px; width: 194px; height: 248px;
    background: linear-gradient(180deg, var(--mascot-back-a), var(--mascot-back-b));
    z-index: 2;
  }

  .wordmark {
    position: absolute;
    text-align: center;
    font-weight: 700;
    line-height: 1.1;
    letter-spacing: 1px;
    text-transform: uppercase;
  }
  .card--front .wordmark {
    left: 228px; top: 290px; width: 360px;
    color: var(--white);
    font-size: 34px;
  }
  .card--back .wordmark {
    left: 408px; top: 290px; width: 320px;
    color: var(--brand-blue);
    font-size: 30px;
  }
  .wordmark .line-small { display: block; font-size: 19px; letter-spacing: 2px; }

  .holder-name {
    position: absolute;
    left: 42px; top: 62px;
    font-size: 27px;
    font-weight: 700;
    color: var(--brand-blue);
    letter-spacing: 0.5px;
    text-transform: uppercase;
  }
  .holder-role {
    position: absolute;
    left: 43px; top: 100px;
    font-size: 15px;
    font-weight: 500;
    color: var(--ink);
    letter-spacing: 0.5px;
  }
  .call-band {
    position: absolute;
    left: 0; top: 192px;
    width: 100%; height: 52px;
    background: linear-gradient(90deg, var(--band-blue-dark), var(--band-blue) 60%, var(--band-blue-dark));
    border-top: 3px solid var(--accent-yellow);
    border-bottom: 3px solid var(--accent-yellow);
  }
  .call-band .call-text {
    position: absolute;
    left: 42px; top: 4px;
    font-size: 29px;
    font-weight: 700;
    color: var(--white);
    letter-spacing: 1.5px;
  }

  .contact-list {
    position: absolute;
    left: 42px; top: 288px;
    list-style: none;
    font-size: 16px;
    color: var(--ink);
    letter-spacing: 0.5px;
  }
  .contact-list li { height: 42px; }
</style>
</head>
<body>

  <section class="card card--front">
    <div class="water-bg" role="img" aria-label="Blue background covered in water droplets"></div>
    <div class="mascot" role="img" aria-label="Cartoon plumber mascot holding a pipe wrench and a circular saw"></div>
    <div class="wordmark">Mossbrook<span class="line-small">Pipeworks &amp; More</span></div>
  </section>

  <section class="card card--back">
    <div class="water-bg" role="img" aria-label="Light grey background covered in water droplets"></div>
    <h1 class="holder-name">Dario Whitlock</h1>
    <p class="holder-role">OWNER</p>
    <div class="call-band"><span class="call-text">Call: (555) 208-7713</span></div>
    <div class="mascot" role="img" aria-label="Cartoon plumber mascot holding a pipe wrench and a circular saw"></div>
    <div class="wordmark">Mossbrook<span class="line-small">Pipeworks &amp; More</span></div>
    <ul class="contact-list">
      <li>Info@mossbrookpipeworks.example</li>
      <li>www.mossbrookpipeworks.example</li>
      <li>License # 5320417</li>
    </ul>
  </section>

</body>
</html>
```